Child Learning Classes Flyer

We have an accelerated learning class and we need a flyer designed that can be delivered in letter boxes and reception areas etc. The flyer needs to be captivating and informative - colourful and intelligent. The classes are right brain classes for children - they improve photographic memory, expose to early literacy, numeracy etc and basically give children a great head start and maximise brain usage…

I need a call to action - something that has a sense of urgency and includes facts - A graph showing a stimulated and unstimulated brain wave pattern or facts like - under the age of 2, there is more brain cell production that at any other time in one's life. If we provide specific stimulation and interaction during this time we have the power to improve brain function for life!

The classes are for babies aged 6 months to children up to the age of 7

Target Market(s)

educated families of moderate to high income

Industry/Entity Type

Learning

Requirements
Must have
• Our logo - can be found at www.brightsproutlab.ae and our contact details

```html
<!DOCTYPE html>
<html lang="en">
<head>
<meta charset="utf-8">
<title>Bright Sprout Lab – Accelerated Learning Flyer</title>
<link rel="stylesheet" href="https://fonts.googleapis.com/css2?family=Bitter:wght@400&family=Quicksand:wght@300;400;500&display=swap">
<style>
  :root {
    --white: #ffffff;
    --teal: #55bec6;
    --teal-deep: #4cb4c2;
    --slate-blue: #4f86a0;
    --orange: #f0974a;
    --grey-text: #8d8d8d;
    --photo-skin: #f2c9a8;
    --photo-hair: #a0643a;
    --photo-teal: #3fb9c4;
  }
  * { margin: 0; padding: 0; box-sizing: border-box; }
  html, body {
    width: 1200px;
    height: 913px;
    overflow: hidden;
    background: var(--white);
  }
  .flyer {
    position: relative;
    width: 1200px;
    height: 913px;
    background: var(--white);
    overflow: hidden;
    font-family: "Quicksand", sans-serif;
  }
  .hero-photo {
    position: absolute;
    left: 562px;
    top: 0;
    width: 638px;
    height: 770px;
    background:
      radial-gradient(circle at 30% 20%, var(--photo-skin) 0 16%, transparent 30%),
      radial-gradient(circle at 78% 30%, var(--photo-skin) 0 18%, transparent 32%),
      radial-gradient(circle at 38% 70%, var(--photo-skin) 0 18%, transparent 32%),
      radial-gradient(circle at 85% 0%, var(--photo-teal) 0 14%, transparent 26%),
      radial-gradient(circle at 55% 50%, var(--photo-hair) 0 22%, transparent 45%),
      linear-gradient(160deg, #fbe6d6, #e9b08a);
  }
  .brand {
    position: absolute;
    left: 40px;
    top: 44px;
    display: flex;
    align-items: center;
    gap: 16px;
  }
  .brand-dot {
    width: 30px;
    height: 30px;
    border-radius: 50%;
    background: var(--orange);
  }
  .brand-name {
    font-family: "Bitter", serif;
    font-weight: 400;
    font-size: 40px;
    line-height: 1.15;
    color: var(--slate-blue);
  }
  .call-to-action {
    position: absolute;
    right: 654px;
    top: 160px;
    text-align: right;
    color: var(--orange);
    font-family: "Bitter", serif;
    font-size: 37px;
    line-height: 56px;
  }
  .divider {
    position: absolute;
    left: 0;
    top: 282px;
    width: 1200px;
    border-top: 3px dashed var(--orange);
  }
  .headline {
    position: absolute;
    right: 654px;
    top: 300px;
    text-align: right;
    font-family: "Bitter", serif;
    font-weight: 400;
    font-size: 80px;
    line-height: 77px;
    letter-spacing: 2px;
  }
  .headline span { display: block; }
  .headline .line-ensure { color: var(--slate-blue); }
  .headline .line-your,
  .headline .line-children { color: var(--orange); }
  .headline .line-future { color: var(--teal-deep); }
  .intro {
    position: absolute;
    left: 9px;
    top: 636px;
    width: 543px;
    color: var(--grey-text);
    font-weight: 300;
    font-size: 22px;
    line-height: 35px;
    text-align: justify;
    text-align-last: right;
  }
  .contact-band {
    position: absolute;
    left: 0;
    top: 770px;
    width: 1200px;
    height: 143px;
    background: var(--teal);
  }
  .contact-list {
    position: absolute;
    left: 36px;
    top: 56px;
    display: flex;
    gap: 20px;
    list-style: none;
    color: var(--white);
    font-weight: 500;
    font-size: 20px;
    white-space: nowrap;
  }
  .contact-list li { display: flex; align-items: center; gap: 5px; }
  .contact-list svg { width: 22px; height: 22px; fill: var(--white); }
  .age-badge {
    position: absolute;
    left: 0;
    top: 0;
    width: 1200px;
    height: 913px;
    pointer-events: none;
  }
  .age-label {
    font-family: "Quicksand", sans-serif;
    font-weight: 500;
    font-size: 66px;
    fill: var(--teal-deep);
  }
  .age-range {
    font-family: "Quicksand", sans-serif;
    font-weight: 500;
    font-size: 28px;
    fill: var(--white);
  }
</style>
</head>
<body>
<main class="flyer">
  <div class="hero-photo" role="img" aria-label="Photograph of four smiling children huddled in a circle, looking down at the camera"></div>

  <div class="brand">
    <span class="brand-dot"></span>
    <span class="brand-name">Bright<br>Sprout Lab</span>
  </div>

  <p class="call-to-action">Call NOW:<br>+971 501234987</p>

  <div class="divider"></div>

  <h1 class="headline">
    <span class="line-ensure">ENSURE</span>
    <span class="line-your">YOUR</span>
    <span class="line-children">CHILDREN’S</span>
    <span class="line-future">FUTURE</span>
  </h1>

  <p class="intro">Our accelerated learning classes are for children aged from 6 months old. The classes are 50 minutes in length and we request a parent or carer to attend the class with the child.</p>

  <footer class="contact-band">
    <ul class="contact-list">
      <li>
        <svg viewBox="0 0 24 24" aria-hidden="true"><path d="M12 1C7.6 1 4.5 4.2 4.5 8.4 4.5 14 12 23 12 23s7.5-9 7.5-14.6C19.5 4.2 16.4 1 12 1zm0 10.2a3 3 0 1 1 0-6 3 3 0 0 1 0 6z"/></svg>
        Dubai, UAE
      </li>
      <li>
        <svg viewBox="0 0 24 24" aria-hidden="true"><path d="M2 5h20v14H2z M3.5 6.5v.4L12 13l8.5-6.1v-.4z M3.5 8.7v8.8h17V8.7L12 14.8z" fill-rule="evenodd"/></svg>
        register@brightsproutlab.ae
      </li>
      <li>
        <svg viewBox="0 0 24 24" aria-hidden="true"><path fill-rule="evenodd" d="M12 2a10 10 0 1 0 0 20 10 10 0 0 0 0-20zm-1 2.1C9.7 5.6 9 7.6 8.8 9.9H4.1A8 8 0 0 1 11 4.1zm2 0a8 8 0 0 1 6.9 5.8h-4.7C15 7.6 14.3 5.6 13 4.1zm-2.2 5.8h2.4c-.2-2-.7-3.6-1.2-4.7-.5 1.1-1 2.7-1.2 4.7zM4.1 11.9h4.7c.2 2.3.9 4.3 2.2 5.8a8 8 0 0 1-6.9-5.8zm6.7 0h2.4c-.2 2-.7 3.6-1.2 4.7-.5-1.1-1-2.7-1.2-4.7zm4.4 0h4.7a8 8 0 0 1-6.9 5.8c1.3-1.5 2-3.5 2.2-5.8z"/></svg>
        www.brightsproutlab.ae
      </li>
    </ul>
  </footer>

  <svg class="age-badge" viewBox="0 0 1200 913" aria-hidden="true">
    <defs>
      <path id="ribbon-curve" d="M780 792 Q930 778 1078 742"/>
    </defs>
    <polygon points="923,523 982,637 1108,658 1018,749 1038,876 923,818 808,876 828,749 738,658 864,637"
             fill="#ffffff" stroke="#f0974a" stroke-width="11" stroke-linejoin="round"/>
    <text class="age-label" x="923" y="722" text-anchor="middle">AGE</text>
    <path d="M780 792 Q930 778 1078 742" fill="none" stroke="#f0974a" stroke-width="46"/>
    <text class="age-range" dy="10"><textPath href="#ribbon-curve" startOffset="50%" text-anchor="middle">6 Months-7 Years</textPath></text>
  </svg>
</main>
</body>
</html>
```